Cinq Leviers SEO Zorvana Plumea ebook cover (2nd of book series) *

Book Title :
Cinq Leviers pour muscler votre Visibilité Organique SEO

Or alternatively if design is better :
SEO : Cinq Leviers pour muscler votre Visibilité Organique

Subtitle : Comment hisser votre page au sommet des annuaires du web

Subject : The book is a very practical how-to guide to help anyone increase dramatically their trafic through SEO (Search Engine Opimization)

It is written in French : so please keep punctuation as provided

The book cover MUST STAND OUT on the Zorvana Plateform as a small Thumbnail (The important words must be readable even at that size : CINQ LEVIERS, Visibilité Organique, SEO) as well as a 6*9 book.

The imagery should make the viewer feel that the book (and the author) are the authority in Search Engine Optimization and Digital Marketing

The readers should feel that they must have this book to increase their site or blog traffic fast.

It is most important that the book “pops off the shelf” and catches the eye quickly. The most important part of the design is that it sells, not that it looks pretty (but it can :-)

Important thing : this cover and ebook is part of a series of books all titled “Cinq Leviers blablabla”. There is already one book of this series published (see cover 5) : Cinq Leviers pour Doubler vos Gains. It’s important that at least one element of this new design recalls the design of the Cover 5 It can be for example the typo for the “7” being the same, or any other idea so that when someone sees both covers, they understand they are from the same series.

I have also enclosed my attempt so that you get the idea I am after, but don’t be too close to it. I am not a designer and I know it is bad, so be free, it is just here to explain the idea of the book cover.
Attached are some covers :
 Covers 1 to 4 are covers I like very much
 Cover 5 is from The first book of the Series : “Cinq Leviers pour Doubler vos Gains” : there should be at least ONE (even tiny) element in common with the new design so that it’s clear they belong to the same series
 Cover 6 is my ugly attempt so that the idea is clear (hopefully)

Target Market(s)

Small entrepreneurs bloggers

Font styles to use
Sans Serif

Colors

Designer to choose colors to be used in the design.

Requirements
Must have
• The book cover MUST STAND OUT on the Zorvana Plateform as a small Thumbnail (The important must be readable even at that size : CINQ LEVIERS, Visibilité Organique, SEO) as well as a 6*9 book.
• Important thing : this cover and ebook is part of a series of books all titled “Cinq Leviers blablabla”. There is already one book of this series published (see cover 5) : Cinq Leviers pour Doubler vos Gains. It’s important that at least one element of this new design recalls the design of the Cover 5 It can be for example the typo for the “7” being the same, or any other idea so that when someone sees both covers, they understand they are from the same series.
• All the texts provided on the brief and my sample cover (6th cover mockup)
• Please enclose the text :
• Checklist SEO Incluse
• In a sticker (see last image as example)
Nice to have
• Nice and simple imagery. Like the one on Cart Sparks. Very simple but also very powerful and meaningful
Should not have
• It should not be as cluttered as my attempt (6th cover enclosed)

```html
<!DOCTYPE html>
<html lang="fr">
<head>
<meta charset="utf-8">
<title>Cinq Leviers pour muscler votre Visibilité Organique SEO</title>
<link rel="stylesheet" href="https://fonts.googleapis.com/css2?family=Archivo+Black&family=Bebas+Neue&family=Oswald:wght@300&display=swap">
<style>
  :root {
    --cover-blue: #0b4f7a;
    --accent-orange: #f7a100;
    --text-white: #ffffff;
    --band-ink: #0b4f7a;
    --art-light: #8fbfd0;
    --art-mid: #5f95ad;
  }
  html, body {
    margin: 0;
    padding: 0;
    overflow: hidden;
  }
  body {
    width: 800px;
    height: 1200px;
  }
  .cover {
    position: relative;
    width: 800px;
    height: 1200px;
    background: var(--cover-blue);
    overflow: hidden;
  }
  .cover-type {
    position: absolute;
    left: 0;
    top: 0;
    width: 800px;
    height: 1200px;
  }
  .series-numeral {
    font-family: "Archivo Black", sans-serif;
    fill: var(--accent-orange);
  }
  .display {
    font-family: "Bebas Neue", sans-serif;
  }
  .light {
    font-family: "Oswald", sans-serif;
    font-weight: 300;
  }
  .fill-white { fill: var(--text-white); }
  .fill-orange { fill: var(--accent-orange); }
  .fill-ink { fill: var(--band-ink); }
  .subtitle-band { fill: var(--accent-orange); }
  .sticker-disc { fill: var(--accent-orange); }
  .hero-art {
    position: absolute;
    left: 280px;
    top: 642px;
    width: 360px;
    height: 292px;
    border-radius: 18px;
    background: radial-gradient(ellipse at 60% 45%, var(--art-light) 0%, var(--art-mid) 55%, var(--cover-blue) 100%);
    opacity: 0.85;
  }
</style>
</head>
<body>
  <main class="cover">
    <div class="hero-art" role="img" aria-label="Illustration : symboles dollar, euro et globe terrestre assemblés comme les lettres SEO, avec de petits ouvriers sur une échelle et une grue"></div>

    <svg class="cover-type" viewBox="0 0 800 1200" role="img" aria-label="Cinq Leviers pour muscler votre Visibilité Organique SEO — Comment hisser votre page au sommet des annuaires du web — Mathis Verlande">
      <text class="series-numeral" x="155" y="282" font-size="150" text-anchor="middle" textLength="296" lengthAdjust="spacingAndGlyphs" transform="rotate(-90 155 228)">CINQ</text>

      <text class="display fill-white" x="286" y="172" font-size="131" letter-spacing="2">LEVIERS</text>
      <text class="light fill-white" x="286" y="242" font-size="58" textLength="476" lengthAdjust="spacingAndGlyphs">POUR MUSCLER VOTRE</text>
      <text class="display fill-orange" x="286" y="324" font-size="97" letter-spacing="1">VISIBILITÉ</text>
      <text class="display fill-white" x="286" y="438" font-size="134" letter-spacing="1">ORGANIQUE</text>
      <text class="display fill-orange" x="284" y="628" font-size="257" letter-spacing="4">SEO</text>

      <g class="sticker">
        <circle class="sticker-disc" cx="150" cy="790" r="92"/>
        <text class="display fill-ink" x="150" y="760" font-size="38" text-anchor="middle" letter-spacing="1">CHECKLIST</text>
        <text class="display fill-ink" x="150" y="820" font-size="64" text-anchor="middle" letter-spacing="2">SEO</text>
        <text class="display fill-ink" x="150" y="856" font-size="38" text-anchor="middle" letter-spacing="1">INCLUSE</text>
      </g>

      <rect class="subtitle-band" x="0" y="956" width="800" height="124"/>
      <text class="light fill-ink" x="400" y="1010" font-size="45" text-anchor="middle">COMMENT HISSER VOTRE PAGE AU SOMMET</text>
      <text class="light fill-ink" x="400" y="1070" font-size="45" text-anchor="middle">DES ANNUAIRES DU WEB</text>

      <text class="display fill-white" x="400" y="1168" font-size="91" text-anchor="middle" letter-spacing="2">MATHIS VERLANDE</text>
    </svg>
  </main>
</body>
</html>
```